Criação de Apres. Comercial (com dobra) para Construção & Engenharia
" Pessoal, vocês verão em documento em anexo que é a versão da nossa página WEB que está em construção que oferecemos serviços de: 1- Reforma & Construção * Projeto Guia de Reforma Fornecemos a planta com alterações e novas medidas. * Orçamento Enviamos nossa proposta de orçamento totalmente grátis. * Acompanhamento de Engenheiro Civil e Arquiteto* Equipe de profissionais capacitados. * Cotação de melhores preços de materiais; Auxiliamos na busca de melhores preços e condições de pagamento para a sua Lar Renovo ou obra. * Seleção de parceiros para execução; Selecionamos profissionais capacitados para a execução da sua Lar Renovo ou obra. 1.1 Assessoria * Acompanhamos o projeto em execução Acompanhamento das atividades associadas ao planejamento, organização, direção e controle necessários para garantir o sucesso da sua Lar Renovo ou obra. * Programação da Obra Compreendendo o detalhamento dos serviços e as providências preliminares, a programação dos materiais, mão de obra e equipamentos. * Relatórios de Andamento da obra Adequação do projeto e da construção às necessidades do cliente no que se refere à qualidade, prazo e custo. 2- Além disso temos a opção:" sua Lar Renovo protegida": * Substituição de materiais danificados Qualquer material danificado por nossos profissionais ou fornecedores são repostos na mesma qualidade e quantidade, sem custos para o cliente. * Correção dos serviços mal executados* Mesmo buscando fornecer o resultado que você espera e sempre trabalhando com profissionais capacitados, erros podem acontecer. Diante disso, asseguramos a conclusão da sua obra com qualidade. * Troca de fornecedor Selecionamos os melhores profissionais do mercado. Mesmo assim, se você não gostar, é livre para nos solicitar a troca. 3- Temos também: "Tudo melhor para você" * Orçamento gratuito * Gestão de pagamento * Prazo e rapidez * Saiba tudo que está acontecendo na sua Lar Renovo * Garantia de Satisfação * Consultoria Técnica * Cronograma de gerenciamento * Otimização de custos * Equipe preparada 4- ORÇAMENTO Vocês verão no documento em anexo que trabalhamos muito com a opção de ORÇAMENTO GRÁTIS. Não se esqueçam de citar isso em nessa apresentação. 5- SEJA NOSSO PARCEIRO Caso sobre espaço no preenchimento do conteúdo. Pode-se aproveitar o campo para PARCEIROS (A empresa trabalha com parceiros/ fornecedores que executam a obra). Pode utilizar o campo orientando o parceiro para entrar no site e se cadastrar. Imagens em anexo irão auxiliá-los. 6-Somos uma empresa NOVA, então não temos nenhum projeto realizado até o momento. OBS IMPORTANTE: - Façam o uso de imagens modernas e suaves.. Queremos ser diferentes e inovadores e precisamos muito da criatividade de vocês. "

```html
<!DOCTYPE html>
<html lang="pt-BR">
<head>
<meta charset="utf-8">
<title>Lar Renovo – Pasta Institucional</title>
<link href="https://fonts.googleapis.com/css2?family=Raleway:wght@300;400;600&display=swap" rel="stylesheet">
<style>
  :root{
    --bg:#e9e9e7;
    --paper:#ffffff;
    --brand-blue:#2a6fb3;
    --brand-blue-light:#5fa0d8;
    --band-grey:#8a8f96;
    --ink:#4a4f57;
    --ink-soft:#7b8089;
    --photo-warm-a:#d9d3cb;
    --photo-warm-b:#8c857d;
    --photo-cool-a:#eeeeec;
    --photo-cool-b:#a9a7a3;
  }
  html,body{margin:0;padding:0;width:1200px;height:1200px;overflow:hidden;background:var(--bg);}
  .canvas{position:relative;width:1200px;height:1200px;font-family:"Raleway",sans-serif;}
  .spread{position:absolute;left:40px;top:205px;width:1120px;height:790px;background:var(--paper);overflow:hidden;box-shadow:0 6px 24px rgba(0,0,0,.15);}
  .spread-art{position:absolute;inset:0;}
  .fold{position:absolute;left:559px;top:0;width:2px;height:100%;background:linear-gradient(to bottom,rgba(0,0,0,.06),rgba(0,0,0,.12));}

  .brand{display:flex;align-items:center;gap:12px;color:var(--brand-blue);font-weight:300;}
  .brand-mark{background:var(--brand-blue);}

  .back-cover{position:absolute;left:0;top:0;width:560px;height:100%;}
  .back-cover .brand{position:absolute;left:205px;top:58px;font-size:26px;gap:9px;}
  .back-cover .brand-mark{width:22px;height:22px;}
  .contact-list{position:absolute;left:165px;top:118px;margin:0;padding:0;list-style:none;color:var(--ink);font-size:14px;}
  .contact-list li{display:flex;align-items:center;gap:10px;margin-bottom:9px;line-height:1.25;}
  .contact-list svg{width:18px;height:18px;flex:none;}

  .front-cover{position:absolute;left:560px;top:0;width:560px;height:100%;}
  .front-cover .brand{position:absolute;left:150px;top:52px;font-size:50px;}
  .front-cover .brand-mark{width:44px;height:44px;}
  .tagline{position:absolute;left:208px;top:118px;font-size:12px;letter-spacing:2.5px;text-transform:uppercase;color:var(--ink-soft);margin:0;}
  .site-url{position:absolute;left:225px;top:488px;font-size:20px;letter-spacing:3px;color:#fff;font-weight:400;text-transform:uppercase;margin:0;}
</style>
</head>
<body>
<div class="canvas">
  <div class="spread">
    <svg class="spread-art" viewBox="0 0 1120 790" xmlns="http://www.w3.org/2000/svg">
      <defs>
        <linearGradient id="bathroomTone" x1="0" y1="0" x2="0.4" y2="1">
          <stop offset="0" stop-color="var(--photo-warm-a)"/>
          <stop offset="1" stop-color="var(--photo-warm-b)"/>
        </linearGradient>
        <linearGradient id="bedroomTone" x1="1" y1="0" x2="0.5" y2="1">
          <stop offset="0" stop-color="var(--photo-cool-a)"/>
          <stop offset="1" stop-color="var(--photo-cool-b)"/>
        </linearGradient>
        <clipPath id="photoArea">
          <path d="M0,372 C320,300 700,350 1120,262 L1120,790 L0,790 Z"/>
        </clipPath>
      </defs>
      <path class="band-grey" d="M0,310 C300,250 700,300 1120,205 L1120,225 C700,318 300,272 0,332 Z" fill="var(--band-grey)" opacity=".75"/>
      <path class="band-blue" d="M0,338 C310,270 700,322 1120,228 L1120,264 C700,352 320,302 0,374 Z" fill="var(--brand-blue)"/>
      <path class="band-blue-light" d="M0,350 C310,286 700,336 1120,242 L1120,252 C700,344 310,296 0,360 Z" fill="var(--brand-blue-light)" opacity=".8"/>
      <g clip-path="url(#photoArea)" role="img" aria-label="Fotografia de interiores modernos: banheiro com banheira branca à esquerda e quarto claro com cama e janelas amplas à direita">
        <rect x="0" y="240" width="560" height="550" fill="url(#bathroomTone)"/>
        <rect x="560" y="240" width="560" height="550" fill="url(#bedroomTone)"/>
      </g>
    </svg>
    <div class="fold"></div>

    <section class="back-cover">
      <div class="brand"><span class="brand-mark"></span><span class="brand-name">Lar Renovo</span></div>
      <ul class="contact-list">
        <li><svg viewBox="0 0 24 24"><circle cx="12" cy="12" r="12" fill="var(--brand-blue)"/><path d="M8.5 6.5l2 .3.8 2.6-1.3 1c.7 1.5 1.8 2.6 3.3 3.3l1-1.3 2.6.8.3 2c-.2.9-1 1.3-2 1.2-4-.5-7.3-3.8-7.8-7.8-.1-1 .3-1.8 1.1-2.1z" fill="#fff"/></svg>(11) 4000-1234</li>
        <li><svg viewBox="0 0 24 24"><circle cx="12" cy="12" r="12" fill="var(--brand-blue)"/><rect x="8.5" y="5.5" width="7" height="13" rx="1.4" fill="#fff"/><rect x="9.7" y="7.2" width="4.6" height="8.5" fill="var(--brand-blue)"/></svg>(11) 98000-5678</li>
        <li><svg viewBox="0 0 24 24"><circle cx="12" cy="12" r="12" fill="var(--brand-blue)"/><rect x="6" y="8" width="12" height="8.5" rx="1" fill="#fff"/><path d="M6.5 8.6L12 13l5.5-4.4" stroke="var(--brand-blue)" stroke-width="1.2" fill="none"/></svg>contato@larrenovo.com.br</li>
        <li><svg viewBox="0 0 24 24"><circle cx="12" cy="12" r="12" fill="var(--brand-blue)"/><path d="M12 5.5a4.2 4.2 0 0 0-4.2 4.2c0 3.2 4.2 8.3 4.2 8.3s4.2-5.1 4.2-8.3A4.2 4.2 0 0 0 12 5.5z" fill="#fff"/><circle cx="12" cy="9.7" r="1.6" fill="var(--brand-blue)"/></svg>Rua das Obras, 120<br>CEP 01000-000</li>
      </ul>
    </section>

    <section class="front-cover">
      <div class="brand"><span class="brand-mark"></span><span class="brand-name">Lar Renovo</span></div>
      <p class="tagline">reforma, construção e assessoria</p>
      <p class="site-url">www.larrenovo.com.br</p>
    </section>
  </div>
</div>
</body>
</html>
```